vLINK ON LLC - New Website Design Help!

Need to build a website that showcases our capabilities. We will be specializing in Government Contracting for SDVOSB set aside and sole source contracts. We provide many services such as Audio & Visual design, install, consulting, all the way through to project completion. Also, IT/Voice infrastructure consulting, design, implementation, project management all the way to project completion.

Target Market(s)

IT/Voice Government Contracts, Managed Service Contracts for Government

Industry/Entity Type

Information Technology and Telecommunications

Coding

Coded - Design and coding required

Number of Pages Required

5+ page

Font styles to use
Other font styles liked:
• Calibri

Colors

Designer to choose only greyscale colors for use in the design.

Requirements
Must have
• Drop downs for additional pages, for About Us, Services, Industry Solutions, Our Company, Contact Us
Nice to have
• Testimonials page or Blog page

```html
<!DOCTYPE html>
<html lang="en">
<head>
<meta charset="utf-8">
<title>vLink On LLC — Government Contracting</title>
<link rel="stylesheet" href="https://fonts.googleapis.com/css2?family=Michroma&family=Inter:wght@400;500;600&display=swap">
<style>
:root{
  --ink:#111111;
  --dark:#2e2f33;
  --mid:#6b6b6b;
  --grey:#8d8d8d;
  --light:#d9d9d9;
  --pale:#efefef;
  --white:#ffffff;
  --line:#9a9a9a;
}
*{box-sizing:border-box;margin:0;padding:0}
html,body{width:1200px;height:4370px;overflow:hidden;background:var(--white)}
body{position:relative;font-family:"Inter",Arial,sans-serif;color:var(--ink)}
.abs{position:absolute}
.display{font-family:"Michroma",Arial,sans-serif;font-weight:400;letter-spacing:1px}
.center{left:0;width:1200px;text-align:center}

/* header */
.site-header{top:0;left:0;width:1200px;height:85px;background:var(--white)}
.brand{left:97px;top:20px;height:45px;display:flex;align-items:center;gap:10px;font-family:"Michroma",sans-serif;font-size:28px;color:var(--ink);letter-spacing:1px}
.brand-square{width:14px;height:14px;background:var(--ink)}
.nav{top:33px;font-family:"Michroma",sans-serif;font-size:12px;color:var(--ink)}
.nav span::after{content:"";display:inline-block;width:5px;height:5px;border-right:1.3px solid var(--ink);border-bottom:1.3px solid var(--ink);transform:rotate(45deg);margin:0 0 3px 5px}

/* hero */
.hero{top:85px;left:0;width:1200px;height:601px;background:linear-gradient(90deg,#7c7c7c 0%,#a8a8a8 40%,#cfcfcf 70%,#bdbdbd 100%)}
.hero-title{left:97px;top:230px;font-size:37px;line-height:66px;color:var(--white);letter-spacing:3px;-webkit-text-stroke:.8px var(--white)}
.hero-text{left:97px;top:364px;width:420px;font-size:14px;line-height:31px;color:var(--white)}
.btn-outline{display:flex;align-items:center;justify-content:space-between;font-family:"Michroma",sans-serif;font-size:13px;padding:0 6px 0 24px}
.btn-outline .arrow{width:50px;height:34px;display:flex;align-items:center;justify-content:center}
.hero-btn{left:97px;top:481px;width:207px;height:48px;border:2px solid var(--white);color:var(--white)}
.hero-btn .arrow{background:var(--white)}
.round-arrow{width:28px;height:28px;border-radius:50%;display:flex;align-items:center;justify-content:center}
.vline{width:1.5px;background:var(--line);left:599px}

/* section headings */
.eyebrow{font-family:"Michroma",sans-serif;font-size:15px;color:var(--mid);letter-spacing:1px}
.heading{font-family:"Michroma",sans-serif;font-size:23px;color:var(--ink);letter-spacing:1px;font-weight:700;-webkit-text-stroke:.7px var(--ink)}

/* mission */
.tagline{left:324px;top:879px;width:552px;height:59px;background:var(--ink);padding:6px}
.tagline-inner{width:100%;height:100%;border:1.5px solid var(--white);display:flex;align-items:center;justify-content:space-between;padding-left:18px;font-family:"Michroma",sans-serif;font-size:14px;color:var(--white);white-space:nowrap;-webkit-text-stroke:.3px var(--white)}
.tagline-tag{background:var(--grey);height:100%;padding:0 14px;display:flex;align-items:center;border-left:6px solid var(--ink)}
.mission-text{left:127px;top:972px;width:946px;text-align:center;font-size:15.5px;line-height:31px;color:#222}
.btn-dark{border:2px solid var(--ink);color:var(--ink);background:var(--white)}
.btn-dark .arrow{background:var(--grey)}

/* services */
.services-band{top:1269px;left:0;width:1200px;height:598px}
.svc-eyebrow{left:97px;top:1365px;font-family:"Michroma",sans-serif;font-size:14px;color:var(--white)}
.svc-title{left:97px;top:1402px;font-family:"Michroma",sans-serif;font-size:23px;color:var(--white);letter-spacing:1px;-webkit-text-stroke:.8px var(--white)}
.svc-text{left:97px;top:1452px;width:310px;font-size:15px;line-height:31px;color:var(--white)}
.svc-btn{left:98px;top:1724px;width:136px;height:43px;background:var(--white);font-family:"Michroma",sans-serif;font-size:12px;display:flex;align-items:center;justify-content:center}
.svc-card{top:1408px;width:207px;height:359px;background:var(--white);text-align:center;padding:31px 12px 0}
.svc-icon{width:95px;height:76px;margin:0 auto 18px;display:flex;align-items:center;justify-content:center}
.svc-card h3{font-family:"Michroma",sans-serif;font-size:15px;line-height:27px;height:54px;display:flex;align-items:center;justify-content:center;font-weight:400;-webkit-text-stroke:.4px var(--ink)}
.svc-card p{font-size:13.5px;line-height:27px;color:#333;margin-top:8px}
.svc-card .more{margin-top:14px}

/* industry */
.ind-tile{top:2070px;width:231px;height:289px}
.ind-caption{position:absolute;left:9px;top:10px;right:9px;bottom:10px;border:2px solid var(--white);display:flex;align-items:flex-end;justify-content:center;padding-bottom:16px;font-family:"Michroma",sans-serif;font-size:14px;color:var(--white);-webkit-text-stroke:.3px var(--white)}

/* testimonials */
.testimonial-band{top:2588px;left:0;width:1200px;height:642px;background:linear-gradient(180deg,#f6f6f6,#e8e8e8)}
.quote-text{left:215px;top:2779px;width:770px;text-align:center;font-size:15px;line-height:31px;color:#222}
.quote-mark{font-family:Georgia,serif;font-size:90px;color:var(--light);line-height:1}
.people{left:60px;top:2958px;width:1080px;height:272px;background:linear-gradient(180deg,#d6d6d6,#8c8c8c 60%,#7a7a7a)}

/* news */
.news-card{top:3418px;width:309px;height:436px;background:var(--white);border:1px solid var(--light)}
.news-card.raised{box-shadow:0 4px 14px rgba(0,0,0,.18)}
.news-img{width:100%;height:165px}
.news-date{position:absolute;left:24px;top:148px;width:124px;height:34px;background:var(--ink);color:var(--white);font-family:"Times New Roman",serif;font-size:15px;display:flex;align-items:center;justify-content:center}
.news-card h3{margin:50px 22px 0;font-family:"Michroma",sans-serif;font-size:15.5px;line-height:30px;font-weight:400;-webkit-text-stroke:.3px var(--ink)}
.news-card p{margin:26px 24px 0;font-size:14px;line-height:30px;color:#555}

/* footer */
.site-footer{top:3946px;left:0;width:1200px;height:424px;background:var(--ink);color:var(--white)}
.foot-brand{left:97px;top:4024px;display:flex;align-items:center;gap:10px;font-family:"Michroma",sans-serif;font-size:24px;color:#8a8a8a;letter-spacing:1px}
.foot-brand .brand-square{background:#8a8a8a}
.social{top:4099px;width:28px;height:28px;border-radius:50%;background:#555}
.badge{top:4166px;width:68px;height:85px;background:#e6e6e6;border:3px solid #cfcfcf}
.foot-h{font-family:"Michroma",sans-serif;font-size:16px;color:var(--white);-webkit-text-stroke:.4px var(--white)}
.foot-links{left:328px;top:4037px;font-size:14.5px;line-height:31px;color:var(--white)}
.foot-links li{list-style:none;display:flex;align-items:center;gap:12px}
.contact-row{left:535px;display:flex;align-items:center;gap:12px;font-size:14.5px;color:var(--white)}
.contact-ico{width:38px;height:38px;border-radius:50%;background:var(--white);display:flex;align-items:center;justify-content:center}
.news-text{left:832px;top:4050px;width:280px;font-size:14.5px;line-height:31px;color:var(--white)}
.email-field{left:832px;top:4120px;width:272px;height:34px;border-bottom:2px solid var(--white);font-size:14.5px;padding-top:6px;color:var(--white)}
.sub-btn{left:832px;top:4200px;width:209px;height:50px;border:2px solid var(--white);color:var(--white)}
.sub-btn .arrow{background:#8a8a8a}
.foot-rule{left:97px;top:4310px;width:1006px;height:1px;background:#777}
.copyright{top:4332px;font-size:14.5px;color:var(--white)}
</style>
</head>
<body>

<header class="site-header abs">
  <div class="brand abs"><span>VLINK ON</span><span class="brand-square"></span></div>
  <nav>
    <div class="nav abs" style="left:448px"><span>About Us</span></div>
    <div class="nav abs" style="left:557px"><span>Services</span></div>
    <div class="nav abs" style="left:667px"><span>Industry Solutions</span></div>
    <div class="nav abs" style="left:855px"><span>Our Company</span></div>
    <div class="nav abs" style="left:1005px"><span>More</span></div>
    <svg class="abs" style="left:1078px;top:31px" width="22" height="22" viewBox="0 0 22 22" fill="none" stroke="#111" stroke-width="1.8"><circle cx="9" cy="9" r="7"/><path d="M14 14l6 6"/></svg>
  </nav>
</header>

<section class="hero abs" role="img" aria-label="Two colleagues reviewing documents together at an office desk"></section>
<h1 class="hero-title display abs">WELCOME TO<br>VLINK ON</h1>
<p class="hero-text abs">Lorem ipsum dolor sit amet, consectetur adipiscing elit, sed do eiusmod tempor incididunt ut labore et dolore magna aliqua.</p>
<a class="hero-btn btn-outline abs">Learn More <span class="arrow"><svg width="30" height="12" viewBox="0 0 30 12" fill="none" stroke="#111" stroke-width="1.6"><path d="M0 6h28M23 1l5 5-5 5"/></svg></span></a>
<div class="round-arrow abs" style="left:30px;top:373px;background:#cfcfcf"><svg width="10" height="12" viewBox="0 0 10 12" fill="none" stroke="#555" stroke-width="2"><path d="M7 1L2 6l5 5"/></svg></div>
<div class="round-arrow abs" style="left:1142px;top:373px;background:#111"><svg width="10" height="12" viewBox="0 0 10 12" fill="none" stroke="#fff" stroke-width="2"><path d="M3 1l5 5-5 5"/></svg></div>

<!-- about / mission -->
<div class="vline abs" style="top:686px;height:44px"></div>
<svg class="abs" style="left:0;top:849px" width="76" height="88"><path d="M0 0L76 44L0 88Z" fill="#e2e2e2"/></svg>
<svg class="abs" style="left:1134px;top:1011px" width="66" height="79"><path d="M66 0L0 40L66 79Z" fill="#e2e2e2"/></svg>
<div class="eyebrow center abs" style="top:779px">ABOUT</div>
<h2 class="heading center abs" style="top:823px">MISSION STATEMENT</h2>
<div class="tagline abs"><div class="tagline-inner">GOVERNMENT CONTRACTING FOR <span class="tagline-tag">SDVOSB</span></div></div>
<p class="mission-text abs">Lorem ipsum dolor sit amet, consectetur adipiscing elit, sed do eiusmod tempor incididunt ut labore et dolore magna aliqua. Ut enim ad minim veniam, quis nostrud exercitation ullamco laboris nisi ut aliquip ex ea commodo consequat. Duis aute irure dolor in reprehenderit in voluptate velit esse cillum dolore eu fugiat nulla pariatur. Excepteur sint occaecat cupidatat non proident, sunt in culpa qui officia deserunt mollit anim id est laborum.</p>
<a class="btn-outline btn-dark abs" style="left:496px;top:1120px;width:208px;height:49px">Learn More <span class="arrow"><svg width="30" height="12" viewBox="0 0 30 12" fill="none" stroke="#fff" stroke-width="1.6"><path d="M0 6h28M23 1l5 5-5 5"/></svg></span></a>
<div class="vline abs" style="top:1222px;height:47px"></div>

<!-- services -->
<svg class="services-band abs" viewBox="0 0 1200 598" role="img" aria-label="Dark toned office backdrop behind the services section"><defs><linearGradient id="svcbg" x1="0" x2="1"><stop offset="0" stop-color="#3a3b3f"/><stop offset=".5" stop-color="#4a4b50"/><stop offset="1" stop-color="#2c2d31"/></linearGradient></defs><path d="M124 0H1200V496L1079 598H0V106Z" fill="url(#svcbg)"/></svg>
<div class="svc-eyebrow abs">SERVICES</div>
<h2 class="svc-title abs">OUR SERVICES</h2>
<p class="svc-text abs">Lorem ipsum dolor sit amet, consectetur adipiscing elit, sed do eiusmod tempor incididunt ut labore et dolore magna aliqua. Ut enim ad minim veniam, quis nostrud exercitation ullamco laboris nisi ut aliquip ex ea commodo consequat. Duis aute irure dolor in reprehenderit in voluptate velit esse cillum dolore eu fugiat nulla pariatur.</p>
<a class="svc-btn abs">Learn More</a>

<article class="svc-card abs" style="left:428px">
  <div class="svc-icon" style="background:#8d8d8d"><svg width="44" height="44" viewBox="0 0 44 44" fill="none" stroke="#fff" stroke-width="1.8"><rect x="12" y="4" width="20" height="14" rx="2"/><path d="M6 30v-4M10 32v-8M14 34v-12M18 30v-4M26 30v-4M30 32v-8M34 34v-12M38 30v-4"/></svg></div>
  <h3>Audio &amp; Visual design</h3>
  <p>Lorem ipsum dolor sit amet, consectetur adipiscing elit, sed do eiusmod tempor magna aliqua.</p>
  <div class="more"><svg width="30" height="14" viewBox="0 0 30 14" fill="none" stroke="#111" stroke-width="1.8"><path d="M0 7h28M22 1l6 6-6 6"/></svg></div>
</article>
<article class="svc-card abs" style="left:660px">
  <div class="svc-icon" style="background:#111"><svg width="44" height="44" viewBox="0 0 44 44" fill="none" stroke="#fff" stroke-width="1.8"><rect x="14" y="4" width="18" height="11"/><circle cx="14" cy="22" r="4"/><path d="M6 36v-4a8 8 0 0116 0v4M22 30h16M4 38h36"/></svg></div>
  <h3>Consulting</h3>
  <p>Lorem ipsum dolor sit amet, consectetur adipiscing elit, sed do eiusmod tempor magna aliqua.</p>
  <div class="more"><svg width="30" height="14" viewBox="0 0 30 14" fill="none" stroke="#111" stroke-width="1.8"><path d="M0 7h28M22 1l6 6-6 6"/></svg></div>
</article>
<article class="svc-card abs" style="left:894px">
  <div class="svc-icon" style="background:#8d8d8d"><svg width="44" height="44" viewBox="0 0 44 44" fill="none" stroke="#fff" stroke-width="1.8"><circle cx="22" cy="18" r="6"/><circle cx="22" cy="18" r="12" stroke-dasharray="4 3"/><path d="M16 36h12M18 40h8"/></svg></div>
  <h3>Project Management</h3>
  <p>Lorem ipsum dolor sit amet, consectetur adipiscing elit, sed do eiusmod tempor magna aliqua.</p>
  <div class="more"><svg width="30" height="14" viewBox="0 0 30 14" fill="none" stroke="#111" stroke-width="1.8"><path d="M0 7h28M22 1l6 6-6 6"/></svg></div>
</article>
<div class="vline abs" style="top:1826px;height:109px"></div>

<!-- industry -->
<div class="eyebrow center abs" style="top:1972px">INDUSTRY</div>
<h2 class="heading center abs" style="top:2013px">INDUSTRY SOLUTIONS</h2>
<div class="ind-tile abs" style="left:98px;background:linear-gradient(160deg,#6f6f6f,#3a3a3a);box-shadow:0 4px 10px rgba(0,0,0,.25)" role="img" aria-label="Professional working at a large digital display wall"><div class="ind-caption">VISUAL DESIGN</div></div>
<div class="ind-tile abs" style="left:355px;background:radial-gradient(circle at 50% 55%,#8a8a8a,#2b2b2b 70%)" role="img" aria-label="Glowing cloud network technology graphic"></div>
<div class="ind-tile abs" style="left:613px;background:linear-gradient(160deg,#b9b9b9,#6d6d6d)" role="img" aria-label="Colleagues meeting around a conference table"></div>
<div class="ind-tile abs" style="left:869px;background:linear-gradient(160deg,#5a5a5a,#a3a3a3)" role="img" aria-label="Excited person celebrating in front of a laptop"></div>
<div class="round-arrow abs" style="left:39px;top:2201px;background:#bdbdbd"><svg width="10" height="12" viewBox="0 0 10 12" fill="none" stroke="#555" stroke-width="2"><path d="M7 1L2 6l5 5"/></svg></div>
<div class="round-arrow abs" style="left:1133px;top:2201px;background:#111"><svg width="10" height="12" viewBox="0 0 10 12" fill="none" stroke="#fff" stroke-width="2"><path d="M3 1l5 5-5 5"/></svg></div>
<a class="btn-outline btn-dark abs" style="left:496px;top:2413px;width:208px;height:49px">Learn More <span class="arrow"><svg width="30" height="12" viewBox="0 0 30 12" fill="none" stroke="#fff" stroke-width="1.6"><path d="M0 6h28M23 1l5 5-5 5"/></svg></span></a>
<div class="vline abs" style="top:2529px;height:59px"></div>

<!-- testimonials -->
<section class="testimonial-band abs"></section>
<div class="eyebrow center abs" style="top:2680px;font-size:13px">WHAT OUR PEOPLE SAYS</div>
<h2 class="heading center abs" style="top:2723px">TESTIMONIALS</h2>
<div class="quote-mark abs" style="left:172px;top:2752px">&ldquo;</div>
<p class="quote-text abs">Sed ut perspiciatis unde omnis iste natus error sit voluptatem accusantium doloremque laudantium, totam rem aperiam, eaque ipsa quae ab illo inventore veritatis et quasi architecto beatae vitae dicta sunt explicabo. Nemo enim ipsam voluptatem quia voluptas sit aspernatur aut odit aut fugit, sed quia consequuntur magni</p>
<div class="quote-mark abs" style="left:968px;top:2838px">&rdquo;</div>
<div class="center abs display" style="top:2893px;font-size:13px;-webkit-text-stroke:.3px #111">DALE MARLOW</div>
<div class="center abs" style="top:2924px;font-size:14px;color:#777">CEO</div>
<div class="round-arrow abs" style="left:39px;top:2810px;background:#bdbdbd"><svg width="10" height="12" viewBox="0 0 10 12" fill="none" stroke="#555" stroke-width="2"><path d="M7 1L2 6l5 5"/></svg></div>
<div class="round-arrow abs" style="left:1133px;top:2810px;background:#111"><svg width="10" height="12" viewBox="0 0 10 12" fill="none" stroke="#fff" stroke-width="2"><path d="M3 1l5 5-5 5"/></svg></div>
<div class="people abs" role="img" aria-label="Row of diverse team members holding laptops, tablets and phones"></div>

<!-- news -->
<div class="eyebrow center abs" style="top:3322px;font-size:13px">BLOG</div>
<h2 class="heading center abs" style="top:3361px">LATEST NEWS</h2>
<article class="news-card abs" style="left:110px">
  <div class="news-img" style="background:linear-gradient(160deg,#8f8f8f,#4d4d4d)" role="img" aria-label="Business team discussing around a desk"></div>
  <div class="news-date">12 Jan 2024</div>
  <h3>Sed ut perspiciatis unde omnis</h3>
  <p>Ut enim ad minima veniam, quis nostrum exercitationem ullamtu corporis suscipit laboriosam, utt nisi ut aliquid ex ea commod.</p>
</article>
<article class="news-card raised abs" style="left:445px">
  <div class="news-img" style="background:linear-gradient(160deg,#d2d2d2,#7b7b7b)" role="img" aria-label="Colleagues reviewing papers in a bright office"></div>
  <div class="news-date">12 Jan 2024</div>
  <h3>Sed ut perspiciatis unde omnis</h3>
  <p>Ut enim ad minima veniam, quis nostrum exercitationem ullamtu corporis suscipit laboriosam, utt nisi ut aliquid ex ea commod.</p>
</article>
<article class="news-card abs" style="left:779px">
  <div class="news-img" style="background:linear-gradient(160deg,#a5a5a5,#5c5c5c)" role="img" aria-label="Team meeting with laptop at a table"></div>
  <div class="news-date">12 Jan 2024</div>
  <h3>Sed ut perspiciatis unde omnis</h3>
  <p>Ut enim ad minima veniam, quis nostrum exercitationem ullamtu corporis suscipit laboriosam, utt nisi ut aliquid ex ea commod.</p>
</article>

<!-- footer -->
<footer class="site-footer abs"></footer>
<div class="foot-brand abs"><span>VLINK ON</span><span class="brand-square"></span></div>
<div class="social abs" style="left:98px"></div>
<div class="social abs" style="left:146px"></div>
<div class="social abs" style="left:194px"></div>
<div class="social abs" style="left:242px"></div>
<div class="badge abs" style="left:98px"></div>
<div class="badge abs" style="left:178px"></div>

<div class="foot-h abs" style="left:328px;top:4008px">Quick Links</div>
<ul class="foot-links abs">
  <li><svg width="14" height="12" viewBox="0 0 14 12" fill="#fff"><path d="M0 5h8V0l6 6-6 6V7H0z"/></svg>About Us</li>
  <li><svg width="14" height="12" viewBox="0 0 14 12" fill="#fff"><path d="M0 5h8V0l6 6-6 6V7H0z"/></svg>Services</li>
  <li><svg width="14" height="12" viewBox="0 0 14 12" fill="#fff"><path d="M0 5h8V0l6 6-6 6V7H0z"/></svg>Industry Solutions</li>
  <li><svg width="14" height="12" viewBox="0 0 14 12" fill="#fff"><path d="M0 5h8V0l6 6-6 6V7H0z"/></svg>Our Company</li>
  <li><svg width="14" height="12" viewBox="0 0 14 12" fill="#fff"><path d="M0 5h8V0l6 6-6 6V7H0z"/></svg>Contact Us</li>
  <li><svg width="14" height="12" viewBox="0 0 14 12" fill="#fff"><path d="M0 5h8V0l6 6-6 6V7H0z"/></svg>More</li>
</ul>

<div class="foot-h abs" style="left:535px;top:4008px">Contact Us</div>
<div class="contact-row abs" style="top:4055px"><span class="contact-ico"><svg width="14" height="18" viewBox="0 0 14 18" fill="#111"><path d="M7 0a7 7 0 017 7c0 5-7 11-7 11S0 12 0 7a7 7 0 017-7zm0 4a3 3 0 100 6 3 3 0 000-6z"/></svg></span>vLink On LLC, Springfield, USA</div>
<div class="contact-row abs" style="top:4115px"><span class="contact-ico"><svg width="16" height="12" viewBox="0 0 16 12" fill="#111"><path d="M0 0h16v12H0zM1 1l7 6 7-6" stroke="#fff" stroke-width="1.2"/></svg></span>hello@vlinkon-example.com</div>
<div class="contact-row abs" style="top:4175px"><span class="contact-ico"><svg width="16" height="16" viewBox="0 0 16 16" fill="#111"><path d="M3 0l3 4-2 2c1 2 3 4 6 6l2-2 4 3-2 3C7 16 0 9 0 3z"/></svg></span>+1 555 014 2290</div>

<div class="foot-h abs" style="left:832px;top:4008px">Sign Up Our Newsletter</div>
<p class="news-text abs">Lorem ipsum dolor sit amet,consectetur adipiscing elit,adipiscing elit.</p>
<div class="email-field abs">Email</div>
<a class="sub-btn btn-outline abs">SUBSCRIBE <span class="arrow"><svg width="30" height="12" viewBox="0 0 30 12" fill="none" stroke="#fff" stroke-width="1.6"><path d="M0 6h28M23 1l5 5-5 5"/></svg></span></a>

<div class="foot-rule abs"></div>
<div class="copyright center abs">Copyrights@2024.vLink On.All Rights Reserved</div>

</body>
</html>
```